Professional juggler and artist needs landing page image

I am a professional juggler and variety artist. I perform my shows all over Europe. My work is fresh, fast paced, feel good and for all ages. I get a lot of inspiration from pop musicians and the way they present themselves.
At the moment I am building my new website and I need an image that will appear on my landing page, just below the header with the menu. The image should be colourful and dynamic with me in the middle. I added some examples in the files.
The dimensions of the final design should be 2:1 (width : height)
Please include my name (MARTIN KOLBERG) in the image and use Bebas Neue as font.

Target Market(s)

Audiences of all ages

Industry/Entity Type

Stage entertainment

Font styles to use
Other font styles liked:
• Bebas Neue

Requirements
Must have
• Pop star look, colourful
Should not have
• A childish look. Also don't make it too "circussy"

```html
<!DOCTYPE html>
<html lang="en">
<head>
<meta charset="utf-8">
<title>Martin Kolberg – Juggler & Variety Artist</title>
<link rel="stylesheet" href="https://fonts.googleapis.com/css2?family=Bebas+Neue&family=Josefin+Sans:wght@600&display=swap">
<style>
  :root {
    --page: #ffffff;
    --ink: #111111;
    --gold: #d9a42c;
    --divider: #9a9a9a;
    --shade: #ececec;
    --stage-deep: #3a0a1c;
    --stage-red: #a3163a;
    --stage-pink: #d94f86;
    --stage-amber: #f1b65a;
    --stage-green: #9ed36a;
    --stage-teal: #3fa7b5;
    --pill-dark: #2a0508;
    --pill-red: #6b0f17;
    --white: #ffffff;
  }
  * { margin: 0; padding: 0; box-sizing: border-box; }
  html, body { width: 1200px; height: 1000px; overflow: hidden; background: var(--page); }
  .canvas { position: relative; width: 1200px; height: 1000px; background: var(--page); }

  .shadow-band {
    position: absolute; left: 0; width: 1200px; height: 45px;
  }
  .shadow-band.top { top: 128px; background: linear-gradient(to bottom, transparent, var(--shade)); }
  .shadow-band.bottom { top: 790px; background: linear-gradient(to bottom, #d8d8d8, transparent); }

  .site-header {
    position: absolute; top: 172px; left: 0; width: 1200px; height: 66px;
    background: var(--page);
  }
  .site-header .corner-panel {
    position: absolute; right: 0; top: 0; width: 150px; height: 64px; background: #fafafa;
  }
  .brand {
    position: absolute; left: 227px; top: 28px; width: 122px; text-align: center; color: var(--ink);
  }
  .brand-name {
    font-family: "Bebas Neue", sans-serif; font-size: 25px; line-height: 22px; letter-spacing: 0.2px;
  }
  .brand-tagline {
    font-family: "Josefin Sans", sans-serif; font-weight: 600; font-size: 9px; line-height: 12px;
  }
  .main-nav {
    position: absolute; left: 592px; top: 31px; display: flex; align-items: center;
    font-family: "Josefin Sans", sans-serif; font-weight: 600; font-size: 11px; letter-spacing: 1.6px;
    color: var(--ink);
  }
  .main-nav .nav-item.active { color: var(--gold); }
  .main-nav .sep { color: var(--divider); margin: 0 16px; font-weight: 400; }

  .hero {
    position: absolute; top: 265px; left: 0; width: 1200px; height: 525px; overflow: hidden;
  }
  .hero-photo {
    position: absolute; inset: 0;
    background:
      radial-gradient(ellipse 180px 260px at 600px 160px, rgba(255,240,170,0.85), transparent 70%),
      radial-gradient(ellipse 120px 300px at 420px 250px, rgba(158,211,106,0.55), transparent 70%),
      radial-gradient(ellipse 120px 300px at 760px 250px, rgba(241,182,90,0.6), transparent 70%),
      radial-gradient(ellipse 100px 280px at 200px 300px, rgba(63,167,181,0.45), transparent 70%),
      radial-gradient(ellipse 110px 260px at 1000px 320px, rgba(217,79,134,0.6), transparent 70%),
      radial-gradient(ellipse 200px 200px at 600px 360px, rgba(120,40,60,0.75), transparent 75%),
      linear-gradient(to bottom, var(--stage-deep) 0%, var(--stage-red) 35%, var(--stage-pink) 60%, #8a3a52 100%);
  }
  .ring { position: absolute; inset: 0; }

  .name-stack {
    position: absolute; left: 0; width: 1200px; text-align: center;
    font-family: "Bebas Neue", sans-serif; font-size: 178px; line-height: 1; letter-spacing: 1px;
  }
  .name-outline {
    color: transparent; -webkit-text-stroke: 1.5px rgba(255,255,255,0.55);
  }
  .name-outline.one { top: 28px; }
  .name-outline.two { top: 160px; -webkit-text-stroke: 1.5px rgba(255,255,255,0.7); }
  .name-main { top: 297px; color: var(--white); }

  .role-pill {
    position: absolute; left: 345px; top: 452px; width: 510px; height: 48px;
    border: 2px solid var(--white); border-radius: 24px;
    background: linear-gradient(to bottom, var(--pill-red), var(--pill-dark));
    color: var(--white); text-align: center;
    font-family: "Bebas Neue", sans-serif; font-size: 33px; line-height: 46px; letter-spacing: 1.6px;
  }
</style>
</head>
<body>
<div class="canvas">
  <div class="shadow-band top"></div>

  <header class="site-header">
    <div class="corner-panel"></div>
    <div class="brand">
      <div class="brand-name">MARTIN KOLBERG</div>
      <div class="brand-tagline">juggler | variety artist</div>
    </div>
    <nav class="main-nav">
      <span class="nav-item active">HOME</span><span class="sep">|</span>
      <span class="nav-item">ABOUT</span><span class="sep">|</span>
      <span class="nav-item">SHOWS</span><span class="sep">|</span>
      <span class="nav-item">VIDEO</span><span class="sep">|</span>
      <span class="nav-item">CONTACT</span>
    </nav>
  </header>

  <section class="hero">
    <div class="hero-photo" role="img" aria-label="Performer in a floral leopard-print shirt juggling pink clubs on a colourful stage with spotlights, bulb lights, red curtains and smoke"></div>

    <svg class="ring" width="1200" height="525" viewBox="0 0 1200 525">
      <circle cx="42" cy="38" r="44" fill="none" stroke="#ffffff" stroke-width="12"/>
      <circle cx="1125" cy="92" r="60" fill="none" stroke="#ffffff" stroke-width="12"/>
      <circle cx="84" cy="510" r="62" fill="none" stroke="rgba(255,255,255,0.45)" stroke-width="12"/>
      <circle cx="1122" cy="510" r="60" fill="none" stroke="rgba(255,255,255,0.45)" stroke-width="12"/>
    </svg>

    <div class="name-stack name-outline one">MARTIN KOLBERG</div>
    <div class="name-stack name-outline two">MARTIN KOLBERG</div>
    <h1 class="name-stack name-main">MARTIN KOLBERG</h1>

    <div class="role-pill">ENERGETIC JUGGLER &amp; VARIETY ARTIST</div>
  </section>

  <div class="shadow-band bottom"></div>
</div>
</body>
</html>
```